Greek Souvlaki Restaurant Menu Design

We would like to redesign our menu (at the moment just a price-list without any graphics) and create something more fun.

You can find all the items we are offering at the following link / our e-shop:
https://olivebranchkitchen.example/orders/en/order/
I have also attached a printout of the above with hand written notes on the sections and items that will be included.

Our menu is divided to a couple of parts:
- Souvlaki Bar and Grill
- Authentic Greek Cuisine
- Wine List
- Desserts
- Bakaliko

This project will take on the first part of our menu, which is the Souvlaki Bar and Grill. If we are happy with your design, we will then develop the rest of our menu.

Souvlaki Bar and Grill
---------------------------

Our souvlaki can be customised to the customer requirements. The following links have similar set ups:

WOW!Patty
https://gr.pinboardly.example/pin/100000000000000001/
I like the way they have set it up, but the graphics and colours used are not my thing. I also like they way they have split up the steps, choose, top it of, etc.

The Krokk
https://gr.pinboardly.example/pin/100000000000000002/
I hate the step 1,2,3 on the left side. It does not make it playful. Like the fact that they have used pictures of the ingredients.

https://gr.pinboardly.example/pin/100000000000000003/
Hate the graphics, like the concept.

-------------

First Sections: Our Souvliaki Pita Wrap

The steps to customise a souvlaki can be found on the following link:
https://olivebranchkitchen.example/orders/en/order/ and choose pita wrap.

Most of the one side of our Souvliaki/Grill menu should be dedicated to our Pita Wraps.

It should have a small description of the Greek Souvlaki Pita Wrap. Something along the lines of "Get a whole meal all wrapped up with our delicious Greek Pita Wraps. Containing protein, sauce and salad". Improvements of this line are welcome.

It should then have the steps to customise it.

Step One.
Choose Base:
1. Chicken Skewer
2. Pork Skewer
3. etc
Price and options can be found on the above link on our website

Step Two.
Add one of our delicious home made sauces.
Options can be found on our website.

Step Three
Finalise it with the ingredients of your choice.
The customer can select multiple incredients

Step Four.
Feeling Hungry? Add extras:
Extras and Prices can be found on the link provided.

Buy two wraps and save. Takeaway only!
You will find this option as "Double Souvlaki Pita Wrap Offer."
Instead of 2x5.5 = £11 pay £10.5. This offer should also be mentioned somewhere on this section.

-----

Second Section - Our Platters

Skewers Platter and Gyros Platter

Options can be found by clicking on the items on the link provided.

Extras and Pita Bread option are common. Meat options are different and skewers have a choice of side. Meat options have 2/3 skewers and 200/300 grams of gyros, so they can probably be combined somehow.

These section can also be called Naked / Open Souvlaki Platters

Third Section
From Our Grill

All options from this section together with modifiers (can be see if you click on each item). I would like pictures from each item.

Forth Section
Meal Deals, starter combo and Set Menu.

Meal Deal for 1/2 and 4 are wraps with extras. The for 4 is not on the pdf and will be up on our website soon, so please check. I think those are easy to e incorporated next to the pita wrap section as upgrades to save.

Set menus are various items.

If they can fit on this page somehow we incorporate them, if not we can make a separate page with the offers / meals deals. If a separate page is created them the meal deal from our kitchen and vegetarean set menu should also be included.

Fifth Section
Salads and Starter

I would like all options from Hot and Cold starter and our salad. I would like pictures next to all options, if possible.

-----

Final notes/ideas.

Wraps, platters and grill could be one page front and back. Salads and starters could be a different page(s) or sections.

The menu should be easily updated and we would like a format where we can update prices and descriptions.

Prices and descriptions can be found on the link provided.

Feel free to improve our descriptions and titles. Please do mention where you made improvements, so we can approve them.

Our kitchen, dessert and wine menu will be given as a separate project and priority will be given to the person that won this competition.

If you need better quality pictures please let us know, most of the pictures we do have them in raw format too.

------

Some designs that I like. To give you an idea of the design I would like to see:

https://www.craftmarketly.example/listing/100000001/american-menu-restaurant-cafe-menus
I would love to see something like that for the grill/salad/starter side of our menu, since it has space for pictures.

https://gr.pinboardly.example/pin/100000000000000004/
I would love to see something like that, where the incredients of a souvlaki come together. This is optional and does not have to be there.

https://gr.pinboardly.example/pin/100000000000000005/

https://gr.pinboardly.example/pin/100000000000000006/

https://gr.pinboardly.example/pin/100000000000000007/

https://gr.pinboardly.example/pin/100000000000000008/

Target Market(s)

London

Font styles to use
Serif
Sans Serif

Colors
abd037
3277b5
33a6d7

Requirements
Must have
• Build your own souvlaki section. See description for examples.

Pictures for starters and salads.

Should be elegant
Nice to have
• Incorporate our relevant meal deals on the souvlaki pita section

```html
<!DOCTYPE html>
<html lang="en">
<head>
<meta charset="utf-8">
<title>Salads and Starters Menu</title>
<link href="https://fonts.googleapis.com/css2?family=Libre+Baskerville&family=EB+Garamond:wght@400;500&family=Lato:wght@400;700&display=swap" rel="stylesheet">
<style>
:root{
  --blue:#3277b5;
  --sky:#33a6d7;
  --green:#abd037;
  --ink:#2b2b2b;
  --muted:#555;
  --paper:#ffffff;
  --wood-light:#f2f2f2;
  --wood-dark:#dcdcdc;
}
*{margin:0;padding:0;box-sizing:border-box}
html,body{width:1200px;height:848px;overflow:hidden;background:var(--paper)}
.spread{position:relative;width:1200px;height:848px;overflow:hidden}
.salad-page{position:absolute;left:0;top:0;width:598px;height:848px;
  background:linear-gradient(160deg,var(--wood-light),var(--wood-dark) 55%,var(--wood-light));}
.starter-page{position:absolute;left:598px;top:0;width:602px;height:848px;background:var(--paper)}
.dish{position:absolute;border-radius:50%}
.salad{position:absolute;text-align:center;font-family:"EB Garamond",serif;color:var(--ink)}
.salad h2{font-family:"Libre Baskerville",serif;font-weight:400;color:var(--blue);font-size:13px;letter-spacing:.3px;line-height:15px}
.salad .price{font-family:"Libre Baskerville",serif;font-size:11px;line-height:14px;margin-top:1px}
.salad p{font-size:11.5px;line-height:12.5px;letter-spacing:.2px}
.page-title{position:absolute;left:666px;top:36px;width:467px;display:flex;align-items:center;gap:10px}
.page-title::before,.page-title::after{content:"";flex:1;height:1px;background:var(--blue)}
.page-title h1{font-family:"Libre Baskerville",serif;font-weight:400;color:var(--blue);font-size:14px;letter-spacing:.4px;white-space:nowrap}
.intro{position:absolute;left:666px;top:62px;width:467px;text-align:center;font-family:"EB Garamond",serif;font-size:6px;color:var(--muted)}
.section-label{position:absolute;display:flex;align-items:center;gap:4px;font-family:"Libre Baskerville",serif;font-size:9px;color:#111}
.section-label span{flex:1;border-bottom:1px dotted #999;height:1px;margin-top:4px}
.pita{position:absolute;width:113px;height:25px;border:1px dotted #999;font-family:"EB Garamond",serif;font-size:5.5px;color:var(--muted)}
.pita b{display:block;text-align:center;font-family:"Lato",sans-serif;font-weight:400;color:var(--sky);font-size:7px;margin-top:2px}
.pita div{display:flex;justify-content:space-around;margin-top:3px}
.pita div i{font-style:normal;border-left:1px solid #ccc;padding-left:3px}
.pita div i:first-child{border:none}
.item{position:absolute;text-align:center;font-family:"EB Garamond",serif;font-size:5.4px;line-height:6.6px;color:var(--muted)}
.item h3{font-family:"Lato",sans-serif;font-weight:400;color:var(--sky);font-size:7px;line-height:9px;margin-bottom:1px}
.item h3 small{color:var(--ink);font-size:5.5px}
.rule{position:absolute;left:666px;top:794px;width:467px;height:1px;background:var(--blue)}
.legend{position:absolute;top:800px;left:666px;width:467px;text-align:center;font-family:"EB Garamond",serif;font-size:5px;color:var(--muted);word-spacing:2px}
.legend span{margin:0 6px}
</style>
</head>
<body>
<main class="spread">
  <section class="salad-page">
    <div class="dish" role="img" aria-label="Photo of Greek salad with feta and olives" style="left:192px;top:94px;width:201px;height:153px;background:radial-gradient(circle at 50% 45%,#f2efe6 18%,#c0392b 38%,#6a8f3a 62%,#f4f4f4 64%)"></div>
    <div class="dish" role="img" aria-label="Photo of Caesar salad with chicken and parmesan" style="left:55px;top:239px;width:220px;height:161px;background:radial-gradient(circle,#e9c96a 30%,#d6b25a 58%,#f5f5f5 62%)"></div>
    <div class="dish" role="img" aria-label="Photo of Cretan dakos salad" style="left:294px;top:239px;width:228px;height:161px;background:radial-gradient(circle,#d94b3a 20%,#b9c980 45%,#f3f3f3 62%)"></div>
    <div class="dish" role="img" aria-label="Photo of halloumi salad with peppers and yogurt dressing" style="left:86px;top:420px;width:208px;height:204px;background:radial-gradient(circle,#ece7d2 22%,#c8402f 40%,#7f9b3e 56%,#f5f5f5 64%)"></div>
    <div class="dish" role="img" aria-label="Photo of side salad with feta" style="left:302px;top:416px;width:208px;height:196px;background:radial-gradient(circle,#e7e2d4 15%,#5f8a36 42%,#f4f4f4 62%)"></div>
    <div class="dish" role="img" aria-label="Photo of house salad with prosciutto and figs" style="left:165px;top:628px;width:424px;height:126px;border-radius:22px;background:radial-gradient(ellipse,#7b2f2a 25%,#5c7a34 55%,#f5f5f5 72%)"></div>

    <article class="salad" style="left:192px;top:32px;width:200px">
      <h2>GREEK SALAD (V)</h2><div class="price">£8.50</div>
      <p>Greek feta, tomato, cucumber,<br>green pepper, onion, olives &amp; olive oil.</p>
    </article>
    <article class="salad" style="left:17px;top:170px;width:160px">
      <h2>CAESAR SALAD</h2><div class="price">£10.00</div>
      <p>Green salad mixed with grilled Chicken Fillet, Cherry Tomatoes, Caesar Sauce &amp; Grated Parmesan.</p>
    </article>
    <article class="salad" style="left:396px;top:169px;width:190px">
      <h2>CRETAN DAKOS SALAD (V)</h2><div class="price">£8.50</div>
      <p>Cretan rusk soaked in Greek extra virgin olive oil, topped with chopped tomato, feta cheese, olives, spring onion &amp; oregano.</p>
    </article>
    <article class="salad" style="left:14px;top:623px;width:150px">
      <h2>HALLOUMI SALAD</h2><div class="price">£8.50</div>
      <p>Halloumi salad with cocktail tomatoes, red and yellow peppers, mix lettuce, cucumber, spring onions and a yogurt &amp; mint dressing.</p>
    </article>
    <article class="salad" style="left:472px;top:562px;width:110px">
      <h2>SIDE SALAD</h2><div class="price">£3.00</div>
      <p>Lettuce, tomato, cucumber, onion and grated feta</p>
    </article>
    <article class="salad" style="left:160px;top:765px;width:300px">
      <h2>OLIVE BRANCH KITCHEN SALAD</h2><div class="price">£9.50 <small style="font-family:'EB Garamond',serif;font-size:10px">(extra Prosciutto + £1.00)</small></div>
      <p>Baby kale, tender baby leaves and a mix of strong and crunchy radicchio, lamb's lettuce and crisp frisee, pomegranate and dry figs. Sautéed with balsamic and honey sauce.</p>
    </article>
  </section>

  <section class="starter-page"></section>

  <header class="page-title"><h1>OUR SALADS AND STARTERS</h1></header>
  <p class="intro">The Greeks often start their meals with a plate of exquisite little treats or starters called Mezedes — "something small and delicate."</p>

  <div class="section-label" style="left:692px;top:101px;width:288px">COLD STARTERS<span></span></div>
  <div class="pita" style="left:981px;top:95px"><b>Pita Bread</b><div><i>Half</i><i>One + £0.50</i><i>Two + £1.50</i></div></div>

  <div class="dish" role="img" aria-label="Photo of tyrokafteri dip" style="left:718px;top:134px;width:76px;height:76px;background:radial-gradient(circle,#e0753a 45%,#f3f3f3 50%,#ddd 70%)"></div>
  <div class="dish" role="img" aria-label="Photo of tzatziki dip" style="left:859px;top:134px;width:76px;height:76px;background:radial-gradient(circle,#f4f1e4 45%,#f3f3f3 50%,#ddd 70%)"></div>
  <div class="dish" role="img" aria-label="Photo of white taramosalata" style="left:996px;top:134px;width:76px;height:76px;background:radial-gradient(circle,#4a2e3a 6%,#ecd9cf 10%,#ecd9cf 45%,#f3f3f3 50%,#ddd 70%)"></div>

  <div class="item" style="left:692px;top:217px;width:128px"><h3>Tyrokafteri (GF) <small>+ £5.00</small></h3>Handmade dip from Greek feta cheese, mild pepper &amp; spices, served with pita bread.</div>
  <div class="item" style="left:833px;top:217px;width:128px"><h3>Tzatziki (GF) <small>+ £4.00</small></h3>Authentic Greek yoghurt, blended with mint, garlic, dill &amp; other herbs. The Greek's favourite dip, served with pita bread.</div>
  <div class="item" style="left:972px;top:217px;width:124px"><h3>White Taramosalata <small>+ £4.00</small></h3>Rich, creamy, made fresh with cod roe, lemon juice, and extra virgin olive oil. Served with pita bread.</div>

  <div class="dish" role="img" aria-label="Photo of marinated Kalamata olives" style="left:703px;top:265px;width:98px;height:80px;border-radius:14px;background:radial-gradient(circle,#3b1f2c 45%,#f2f2f2 62%)"></div>
  <div class="dish" role="img" aria-label="Photo of hummus" style="left:830px;top:280px;width:133px;height:65px;border-radius:10px;background:radial-gradient(ellipse,#d9c48a 35%,#f3f3f3 60%)"></div>
  <div class="dish" role="img" aria-label="Photo of feta cheese with oregano" style="left:983px;top:273px;width:96px;height:68px;background:radial-gradient(ellipse,#f6f3e6 40%,#e3e3e3 60%)"></div>

  <div class="item" style="left:688px;top:349px;width:128px"><h3>Marinated Kalamata<br>Giant Olives (V) <small>+ £5.80</small></h3>The Kalamata olive is a large, black olive with a smooth, meaty texture named after the city of Kalamata in the southern Peloponnese, Greece. Perfect to nibble on before or in between meals.</div>
  <div class="item" style="left:832px;top:349px;width:128px"><h3>Hummus <small>+ £4.00</small></h3>Pureed chickpeas, tahini, lemon, garlic drizzled with extra virgin olive oil served with pita bread.</div>
  <div class="item" style="left:972px;top:349px;width:124px"><h3>Feta Cheese (GF) <small>+ £5.00</small></h3>Greek feta in extra virgin olive oil, dusted with oregano.</div>

  <div class="section-label" style="left:696px;top:440px;width:288px">HOT STARTERS<span></span></div>
  <div class="pita" style="left:985px;top:434px"><b>Pita Bread</b><div><i>Half</i><i>One + £0.50</i><i>Two + £1.50</i></div></div>

  <div class="dish" role="img" aria-label="Photo of gigantes beans in tomato sauce" style="left:721px;top:480px;width:78px;height:78px;background:radial-gradient(circle,#d2552e 55%,#9fc1c4 60%)"></div>
  <div class="dish" role="img" aria-label="Photo of grilled halloumi with lemon" style="left:849px;top:480px;width:105px;height:77px;background:radial-gradient(ellipse,#e8d9a8 45%,#f2f2f2 62%)"></div>
  <div class="dish" role="img" aria-label="Photo of fries dusted with oregano" style="left:987px;top:480px;width:100px;height:77px;background:radial-gradient(ellipse,#e3a734 45%,#f2f2f2 62%)"></div>

  <div class="item" style="left:692px;top:561px;width:128px"><h3>Gigantes Starter (V) <small>+ £4.00</small></h3>A classic Greek recipe, consisting of giant beans baked in a tomato sauce along with plenty of fresh herbs.</div>
  <div class="item" style="left:838px;top:561px;width:128px"><h3>Grilled Halloumi (V) <small>+ £5.00</small></h3>The favourite Cypriot cheese served with lemon slices &amp; fresh mint.</div>
  <div class="item" style="left:978px;top:561px;width:124px"><h3>Fries (V) <small>+ £4.00</small></h3>Crunchy fries dusted with coarse salt &amp; oregano.</div>

  <div class="dish" role="img" aria-label="Photo of fava split pea puree with capers" style="left:787px;top:608px;width:80px;height:79px;border-radius:18px;background:radial-gradient(circle,#e5b64a 45%,#f2f2f2 62%)"></div>
  <div class="dish" role="img" aria-label="Photo of baked feta in filo with honey and sesame" style="left:917px;top:607px;width:102px;height:84px;background:radial-gradient(circle,#cf8a3c 38%,#f2f2f2 58%)"></div>

  <div class="item" style="left:763px;top:695px;width:128px"><h3>Fava Starter <small>+ £4.00</small></h3>Authentic Santorini Island yellow split pea puree. Served with capers and a variety of mixed onions.</div>
  <div class="item" style="left:904px;top:695px;width:128px"><h3>Baked Feta Cheese<br>with Honey and Sesame <small>+ £6.00</small></h3>Feta cheese wrapped in filo pastry with honey and sesame.</div>

  <div class="rule"></div>
  <p class="legend"><span>(GF) Gluten Free</span><span>(V) Vegetarian</span><span>(N) May Contain Nuts</span></p>
</main>
</body>
</html>
```